4 'Thank you' greetings cards designs

We are a small greetings card publisher and we need designs for a range of 'Thank you' greetings cards and notecards.
This project is for a total of 4 designs.
Please take a look at this board on Clipnest, to see the kind of thing we are looking for: https://www.pinboardly.example/marvk8150/gratitude-notes/
The cards will be printed at a maximum size of 131mm x 183mm (including a 3mm bleed) so please provide 300dpi CMYK files at this size. Please ensure that any text (or elements of the design that are not part of the bleed) are at least 11mm in from each edge. Also, please note that cards do not have to have a bleed if your design doesn't require it (e.g. a plain white background).
Please provide 2 designs in 'portrait' orientation and 2 in 'landscape'.
Please provide 2 designs that just have the words 'Thank you' and then 2 designs that include your choice of these alternative messages:
Thank you so much
Thanks very much
Thank you very much
Thanks a million
Just to say thank you
A big thank you
A really big thank you
Feel free to use an exclamation mark on a couple of your designs, if you wish!
Other than the above guidelines, everything else is up to you in terms of colours, fonts, shapes, etc. - but please use the Clipnest board to see the kind of designs we are looking for.
Thank you!

```html
<!DOCTYPE html>
<html lang="en">
<head>
<meta charset="utf-8">
<title>Thank You Cards</title>
<link rel="stylesheet" href="https://fonts.googleapis.com/css2?family=Lobster&display=swap">
<style>
  :root {
    --paper: #ffffff;
    --backdrop: #ffffff;
    --orange: #ff5a0a;
    --yellow: #ffe500;
    --lime: #b8f000;
    --green: #2fb84a;
    --navy: #0d3a5c;
  }
  html, body {
    margin: 0;
    padding: 0;
    width: 1200px;
    height: 1200px;
    overflow: hidden;
    background: var(--backdrop);
  }
  .canvas {
    position: relative;
    width: 1200px;
    height: 1200px;
  }
  .card {
    position: absolute;
    width: 760px;
    height: 545px;
    background: var(--paper);
    overflow: hidden;
    outline: 1px solid #ececec;
  }
  .card--thank-you { left: 210px; top: 22px; }
  .card--so-much { left: 206px; top: 626px; }
  .spray {
    position: absolute;
    inset: 0;
    width: 100%;
    height: 100%;
  }
  .greeting {
    position: absolute;
    margin: 0;
    font-family: "Lobster", cursive;
    font-weight: 400;
    line-height: 1;
    white-space: nowrap;
    transform: translate(-50%, -50%);
  }
  .greeting--bold {
    color: var(--orange);
    font-size: 150px;
    text-shadow:
      3px 3px 0 var(--paper),
      6px 6px 0 var(--orange),
      7px 7px 0 var(--orange);
  }
  .greeting--bold.line-1 { left: 380px; top: 180px; transform: translate(-50%, -50%) rotate(-6deg); }
  .greeting--bold.line-2 { left: 358px; top: 340px; transform: translate(-50%, -50%) rotate(-6deg); }
  .greeting--retro {
    color: var(--orange);
    font-size: 72px;
    text-shadow:
      2px 2px 0 var(--yellow),
      4px 4px 0 var(--lime),
      6px 6px 0 var(--green);
  }
  .greeting--retro.line-1 { left: 396px; top: 210px; }
  .greeting--retro.line-2 { left: 400px; top: 296px; }
</style>
</head>
<body>
<main class="canvas">

  <section class="card card--thank-you">
    <svg class="spray" viewBox="0 0 760 545" role="img" aria-label="Diagonal spray-paint bands in navy, green, lime, yellow and orange either side of a white panel">
      <defs>
        <filter id="soft-edge" x="-20%" y="-20%" width="140%" height="140%">
          <feGaussianBlur stdDeviation="7"/>
        </filter>
        <linearGradient id="band-left" x1="1" y1="0" x2="0" y2="1">
          <stop offset="0.15" stop-color="var(--navy)"/>
          <stop offset="0.38" stop-color="var(--green)"/>
          <stop offset="0.55" stop-color="var(--lime)"/>
          <stop offset="0.68" stop-color="var(--yellow)"/>
          <stop offset="0.85" stop-color="var(--orange)"/>
        </linearGradient>
        <linearGradient id="band-right" x1="1" y1="0" x2="0" y2="1">
          <stop offset="0.2" stop-color="var(--navy)"/>
          <stop offset="0.4" stop-color="var(--green)"/>
          <stop offset="0.55" stop-color="var(--lime)"/>
          <stop offset="0.68" stop-color="var(--yellow)"/>
          <stop offset="0.85" stop-color="var(--orange)"/>
        </linearGradient>
      </defs>
      <g filter="url(#soft-edge)">
        <polygon points="180,24 340,24 250,360 48,348" fill="url(#band-left)"/>
        <polygon points="612,236 744,216 676,540 444,528" fill="url(#band-right)"/>
      </g>
      <polygon class="panel" points="200,60 560,160 470,500 110,400" fill="var(--paper)" transform="rotate(-12 335 280)"/>
    </svg>
    <p class="greeting greeting--bold line-1">Thank</p>
    <p class="greeting greeting--bold line-2">You</p>
  </section>

  <section class="card card--so-much">
    <svg class="spray" viewBox="0 0 760 545" role="img" aria-label="Horizontal spray-paint cloud in yellow, lime, green and navy behind a white circle">
      <defs>
        <filter id="cloud-edge" x="-20%" y="-20%" width="140%" height="140%">
          <feGaussianBlur stdDeviation="14"/>
        </filter>
        <linearGradient id="cloud-bands" x1="0" y1="0" x2="0" y2="1">
          <stop offset="0.1" stop-color="var(--yellow)"/>
          <stop offset="0.35" stop-color="var(--lime)"/>
          <stop offset="0.55" stop-color="var(--green)"/>
          <stop offset="0.75" stop-color="var(--navy)"/>
        </linearGradient>
      </defs>
      <g filter="url(#cloud-edge)">
        <path d="M40,170 C120,110 260,120 400,100 C520,80 600,40 700,70 C740,150 730,330 700,420 C600,480 500,450 400,440 C280,440 180,470 60,430 C30,340 20,250 40,170 Z" fill="url(#cloud-bands)"/>
      </g>
      <circle cx="398" cy="250" r="162" fill="var(--paper)"/>
    </svg>
    <p class="greeting greeting--retro line-1">Thank You</p>
    <p class="greeting greeting--retro line-2">So Much</p>
  </section>

</main>
</body>
</html>
```